Improve Wine Bottle Label, Glass Printed Naked Lady, Elegant, Classy, Professional

We are transitioning our labelling method over to glass screen-printing.We have an existing label (attached image1 -ai also attached) that we think is cool, but moving forward we would like a more professional looking design that is classy, artsy, but still high impact (one very rough idea is attached). The bottle is remaining the same size. The cap is the same pink colour. Title of wine is The Quiet Harbour' Front Text needs to include:2018 MontepulcianoEden Valley - Barossa The graphic must contain a tasteful (arty) and attractive naked woman. Design colours that are preferred are:Hot Pink - as seen in imageDark Blue - as seen in imageMatte White** Note that colours are single, shading etc is not easily possible due to the screen printing method. - view process on our instagram page. https://www.instagram.com/tvelwinehouse/- please also look at this page to see our other recent labels, so ascertain our style/audience.You do not need to have all the colours, if your submission looks great with 1 or 2. feel free to keep it this way. Dimensions.The glass printer can print within 10mm of the base of the bottle, and 10mm of the shoulder of the bottle. Height 150mmIt can print the full circumference of the bottle up to approx 30mm gap. (Max 208mm) - see our gold label on the instagram page. - however, imagine this bottle in a store - we need customers to be able to see the image and title on one side. So if you decide to wrap around the bottle, it needs to achieve the requirements whilst only seeing the Title side of the bottle. We have found this to be about 90mm wide maximum.

Target Market(s)

Wine Consumers

Industry/Entity Type

Winery

Font styles to use
Serif
Sans Serif

Colors
e34297
3176b5
ffffff

Requirements
Must have
• Colours, Title, Text - as stated
• Naked arty woman
• Single colours - NO SHADING
Nice to have
• Our Logo integrated smoothly - only do this if you can do it well.

```html
<!DOCTYPE html>
<html lang="en">
<head>
<meta charset="utf-8">
<title>The Quiet Harbour – 2018 Montepulciano</title>
<link rel="stylesheet" href="https://fonts.googleapis.com/css2?family=Bebas+Neue&family=Crimson+Text&display=swap">
<style>
  :root {
    --backdrop: #eceeee;
    --panel: #ffffff;
    --glass: #0d0a0b;
    --cap: #b8348f;
    --cap-light: #c66bb0;
    --hot-pink: #e6157f;
    --gold: #c9a24a;
    --gold-light: #efd48a;
    --white: #ffffff;
  }
  html, body {
    margin: 0;
    padding: 0;
    width: 756px;
    height: 1200px;
    overflow: hidden;
    background: var(--backdrop);
  }
  .canvas { display: block; width: 756px; height: 1200px; }
  .panel { fill: var(--panel); }
  .glass { fill: var(--glass); }
  .cap { fill: var(--cap); }
  .cap-highlight { fill: var(--cap-light); }
  .title {
    font-family: "Bebas Neue", "Arial Narrow", sans-serif;
    fill: var(--white);
  }
  .varietal-small {
    font-family: "Crimson Text", "Times New Roman", serif;
    fill: var(--hot-pink);
    font-size: 12.5px;
  }
  .varietal-large {
    font-family: "Crimson Text", "Times New Roman", serif;
    fill: var(--white);
    font-size: 20px;
  }
  .band-pink { fill: var(--hot-pink); }
  .brand-mark circle { fill: none; stroke: var(--white); stroke-width: 1.5; }
  .brand-name {
    font-family: "Crimson Text", "Times New Roman", serif;
    fill: var(--white);
    font-size: 11px;
  }
</style>
</head>
<body>
<svg class="canvas" viewBox="0 0 756 1200" xmlns="http://www.w3.org/2000/svg">
  <defs>
    <linearGradient id="pink-figure" x1="0" y1="0" x2="0" y2="1">
      <stop offset="0" stop-color="#e6157f" stop-opacity="0.35"/>
      <stop offset="1" stop-color="#e6157f" stop-opacity="0.15"/>
    </linearGradient>
    <linearGradient id="gold-figure" x1="0" y1="0" x2="1" y2="1">
      <stop offset="0" stop-color="#efd48a" stop-opacity="0.35"/>
      <stop offset="1" stop-color="#b8862e" stop-opacity="0.15"/>
    </linearGradient>
    <linearGradient id="gold-band" x1="0" y1="0" x2="1" y2="0">
      <stop offset="0" stop-color="#a97d2a"/>
      <stop offset="0.5" stop-color="#efd48a"/>
      <stop offset="1" stop-color="#a97d2a"/>
    </linearGradient>
  </defs>

  <rect class="panel" x="92" y="52" width="568" height="1083"/>

  <!-- Bottle: pink edition -->
  <g class="bottle bottle--pink">
    <path class="glass" d="M188,182 L263,182 L263,300 C263,350 343,362 343,432 L343,1118 Q343,1130 331,1130 L120,1130 Q108,1130 108,1118 L108,432 C108,362 188,350 188,300 Z"/>
    <rect class="cap" x="183" y="60" width="85" height="124" rx="6"/>
    <rect class="cap-highlight" x="183" y="60" width="26" height="124" rx="6"/>

    <rect role="img" aria-label="Pink single-line drawing of an artistic nude woman with flowing hair, standing on one leg" x="130" y="505" width="140" height="440" rx="60" fill="url(#pink-figure)"/>

    <g class="brand-mark">
      <circle cx="298" cy="531" r="19"/>
      <text class="brand-name" x="298" y="535" text-anchor="middle">Tvel</text>
    </g>

    <text class="title" font-size="42">
      <tspan x="208" y="858">THE</tspan>
      <tspan x="208" y="901">QUIET</tspan>
      <tspan x="208" y="944">HARBOUR</tspan>
    </text>
    <text class="varietal-small" x="208" y="964">2018 Montepulciano</text>
    <text class="varietal-small" x="208" y="977">Eden Valley - Barossa</text>

    <rect class="band-pink" x="108" y="987" width="235" height="7"/>
    <rect x="108" y="1000" width="235" height="2" fill="url(#gold-band)"/>
  </g>

  <!-- Bottle: gold edition -->
  <g class="bottle bottle--gold">
    <path class="glass" d="M478,182 L553,182 L553,300 C553,350 640,362 640,432 L640,1118 Q640,1130 628,1130 L405,1130 Q393,1130 393,1118 L393,432 C393,362 478,350 478,300 Z"/>
    <rect class="cap" x="473" y="60" width="85" height="124" rx="6"/>
    <rect class="cap-highlight" x="473" y="60" width="26" height="124" rx="6"/>

    <rect role="img" aria-label="Gold single-line drawing of an artistic nude woman standing on one leg" x="488" y="500" width="140" height="450" rx="60" fill="url(#gold-figure)"/>

    <text class="title" font-size="60" letter-spacing="3" transform="translate(482 930) rotate(-90)">THE QUIET HARBOUR</text>

    <g class="brand-mark">
      <circle cx="590" cy="840" r="19"/>
      <text class="brand-name" x="590" y="844" text-anchor="middle">Tvel</text>
    </g>

    <text class="varietal-large" x="432" y="982">2018 Montepulciano</text>
    <text class="varietal-large" x="432" y="1007">Eden Valley - Barossa</text>

    <rect class="band-pink" x="393" y="1020" width="247" height="7"/>
    <rect x="393" y="1033" width="247" height="2" fill="url(#gold-band)"/>
  </g>
</svg>
</body>
</html>
```